Charting 2030 book cover

As part of the Meridian Forum's partnership with the Federal Insight Board, we will be releasing a response report to their World Currents 2030 release. This report will be published as a printed soft cover book(about 100 pgs), as well as an ebook. The size will be approximately 6"x9" with glued binding, so the design could feasibly wrap around.

The report illustrates steps the US needs to take to have a bright and prosperous future in 2030. The world is changing, and we have to prepare for the developing new environment.

Words that come to mind: future, horizon, global, hope, dawn
Concepts that come to mind: sunrise (from space), fork in the road, road map, labyrinth
Updates

I've been asked if we can move the deadline to the previous Friday from the current date of 12/3. Submissions on or before 11/30/2012 are appreciated.

Target Market(s)

intelligence community, think tanks

Industry/Entity Type

Environment

Requirements
Must have
• Name of the report:
Charting 2030: US Policy for a Multipolar Age

Author:
Daniel P. Whitcombe
Long Horizon Project, Harold Lindqvist Center on Global Stability

Logo:
Meridian Forum (uploaded along with branding guidelines)
Should not have
• This should not look like a standard academic report/publication.

```html
<!DOCTYPE html>
<html lang="en">
<head>
<meta charset="utf-8">
<title>Charting 2030 – Wraparound Cover</title>
<link href="https://fonts.googleapis.com/css2?family=Oswald:wght@700&family=Merriweather:wght@400;700&family=Open+Sans:wght@400;700&display=swap" rel="stylesheet">
<style>
  :root {
    --stage-light: #e4e4e4;
    --stage-dark: #c8c8c8;
    --label: #111111;
    --navy-top: #0b5198;
    --navy-mid: #0a3a78;
    --navy-deep: #020a22;
    --spine-top: #0a4489;
    --spine-bottom: #03102c;
    --white: #ffffff;
    --silver: #d9dce2;
    --accent-blue: #1f8fe2;
    --sun-core: #fffbe8;
    --sun-glow: #ffd84a;
    --sun-amber: #e08a1c;
    --earth-brown: #6b3e1a;
  }
  * { box-sizing: border-box; margin: 0; padding: 0; }
  html, body { width: 1200px; height: 780px; overflow: hidden; }
  body {
    position: relative;
    background: radial-gradient(ellipse at 50% 40%, var(--stage-light), var(--stage-dark));
    font-family: "Open Sans", sans-serif;
  }

  .panel-label {
    position: absolute;
    top: 20px;
    font-family: "Open Sans", sans-serif;
    font-weight: 700;
    font-size: 17px;
    color: var(--label);
    transform: translateX(-50%);
  }
  .panel-label--back { left: 330px; }
  .panel-label--spine { left: 600px; }
  .panel-label--front { left: 877px; }

  .cover {
    position: absolute;
    left: 102px;
    top: 47px;
    width: 998px;
    height: 718px;
    overflow: hidden;
  }

  /* ---------- back ---------- */
  .back {
    position: absolute;
    left: 0; top: 0;
    width: 480px; height: 718px;
    color: var(--white);
  }
  .back__art {
    position: absolute; inset: 0;
    background:
      radial-gradient(ellipse 70% 45% at 25% 30%, rgba(90,150,210,0.55), transparent 70%),
      linear-gradient(180deg, var(--navy-top) 0%, #0a468a 35%, var(--navy-mid) 60%, var(--navy-deep) 100%);
  }
  .back__heading {
    position: absolute;
    top: 18px; left: 0; width: 100%;
    text-align: center;
  }
  .back__title {
    font-family: "Oswald", sans-serif;
    font-weight: 700;
    font-size: 25px;
    line-height: 30px;
    letter-spacing: 2px;
    color: var(--silver);
  }
  .back__rule {
    width: 180px; height: 1px;
    margin: 3px auto 4px;
    background: var(--white);
  }
  .back__subtitle {
    font-family: "Merriweather", serif;
    font-weight: 700;
    font-size: 10.5px;
  }
  .back__blurb {
    position: absolute;
    top: 150px; left: 22px; width: 436px;
    text-align: center;
    font-size: 11.6px;
    line-height: 16px;
  }
  .back__blurb p + p { margin-top: 16px; }
  .back__brand { position: absolute; left: 20px; bottom: 26px; }

  /* ---------- spine ---------- */
  .spine {
    position: absolute;
    left: 480px; top: 0;
    width: 39px; height: 718px;
    background: linear-gradient(180deg, var(--spine-top), var(--navy-mid) 45%, var(--spine-bottom));
  }
  .spine__title {
    position: absolute;
    top: 115px; left: 50%;
    transform: translateX(-50%);
    writing-mode: vertical-rl;
    white-space: nowrap;
  }
  .spine__main {
    font-family: "Oswald", sans-serif;
    font-weight: 700;
    font-size: 17px;
    letter-spacing: 1.5px;
    color: var(--white);
  }
  .spine__sub {
    font-family: "Merriweather", serif;
    font-size: 10.5px;
    color: var(--accent-blue);
    margin-top: 4px;
  }
  .spine__author {
    position: absolute;
    top: 570px; left: 50%;
    transform: translateX(-50%);
    writing-mode: vertical-rl;
    white-space: nowrap;
    font-family: "Merriweather", serif;
    font-weight: 700;
    font-size: 10.5px;
    letter-spacing: 0.5px;
    color: var(--white);
  }

  /* ---------- front ---------- */
  .front {
    position: absolute;
    left: 519px; top: 0;
    width: 479px; height: 718px;
    color: var(--white);
  }
  .front__art {
    position: absolute; inset: 0;
    background:
      radial-gradient(circle at 50% 55%, var(--sun-core) 0%, rgba(255,245,190,0.95) 7%, rgba(255,216,74,0.8) 16%, rgba(224,138,28,0.45) 32%, transparent 55%),
      radial-gradient(ellipse 130% 60% at 50% 90%, rgba(200,140,40,0.75) 0%, var(--earth-brown) 45%, transparent 80%),
      linear-gradient(180deg, var(--navy-top) 0%, #0b3b74 14%, #1e2c4a 30%, #5a4030 50%, #7a4c20 70%, #2a1a0c 90%, #000000 100%);
  }
  .front__brand { position: absolute; left: 19px; top: 33px; }
  .front__title {
    position: absolute;
    top: 82px; left: 0; width: 100%;
    text-align: center;
    font-family: "Oswald", sans-serif;
    font-weight: 700;
    font-size: 60px;
    line-height: 72px;
    letter-spacing: 5px;
    color: var(--silver);
    text-shadow: 0 2px 4px rgba(0,0,0,0.6);
  }
  .front__subtitle {
    position: absolute;
    top: 229px; left: 0; width: 100%;
    text-align: center;
    font-family: "Merriweather", serif;
    font-weight: 700;
    font-size: 19px;
    text-shadow: 0 1px 3px rgba(0,0,0,0.6);
  }
  .front__author {
    position: absolute;
    top: 645px; left: 0; width: 100%;
    text-align: center;
    font-family: "Merriweather", serif;
    font-weight: 700;
    font-size: 21px;
    letter-spacing: 1.5px;
    color: var(--accent-blue);
  }
  .front__affiliation {
    position: absolute;
    top: 680px; left: 0; width: 100%;
    text-align: center;
    font-size: 10.5px;
    line-height: 14px;
  }

  /* ---------- brand mark ---------- */
  .brand {
    display: flex;
    align-items: center;
    gap: 6px;
    font-family: "Merriweather", serif;
    font-weight: 400;
    font-size: 15px;
    color: var(--white);
    white-space: nowrap;
  }
  .brand__dot {
    width: 25px; height: 25px;
    border-radius: 50%;
    background: var(--white);
  }
</style>
</head>
<body>
  <div class="panel-label panel-label--back">BACK</div>
  <div class="panel-label panel-label--spine">SPINE</div>
  <div class="panel-label panel-label--front">FRONT</div>

  <div class="cover">
    <section class="back">
      <div class="back__art" role="img" aria-label="Deep blue view of Earth from space fading into darkness"></div>
      <div class="back__heading">
        <div class="back__title">CHARTING<br>2030:</div>
        <div class="back__rule"></div>
        <div class="back__subtitle">US Policy for a Multipolar Age</div>
      </div>
      <div class="back__blurb">
        <p>Lorem ipsum dolor sit amet, consectetur adipiscing elit. Vestibulum vulputate augue eu ipsum luctus sit amet vestibulum nulla gravida. Nunc at nulla ante. Donec nec dui ornare justo elementum molestie eget nec ipsum. Donec interdum tincidunt odio, eu fringilla quam accumsan et. Donec lectus odio, varius et faucibus quis, feugiat vitae urna. Fusce orci nibh, facilisis non lobortis aliquet, ultrices a urna. Cras tellus ipsum, viverra ac iaculis at, aliquam quis nibh.</p>
        <p>Donec nisl ante, tempus non aliquet id, posuere id quam. Nulla risus elit, vehicula eu dolor. Nunc non ullamcorper erat. Suspendisse potenti. Pellentesque diam risus, tempor ac mollis nec, fermentum id augue. Vestibulum ut tellus eros, tincidunt volutpat nibh. Aliquam semper, turpis id malesuada sollicitudin, nisl leo condimentum sapien, tempor suscipit leo lacus non lacus. Etiam rutrum nisi ac nisl aliquam pretium tempus quam fermentum.</p>
      </div>
      <div class="brand back__brand"><span class="brand__dot"></span>Meridian Forum</div>
    </section>

    <section class="spine">
      <div class="spine__title"><span class="spine__main">CHARTING 2030:</span><span class="spine__sub">US Policy for a Multipolar Age</span></div>
      <div class="spine__author">DANIEL P. WHITCOMBE</div>
    </section>

    <section class="front">
      <div class="front__art" role="img" aria-label="Sunrise over the curve of the Earth seen from space, glowing gold against deep blue"></div>
      <div class="brand front__brand"><span class="brand__dot"></span>Meridian Forum</div>
      <h1 class="front__title">CHARTING<br>2030:</h1>
      <div class="front__subtitle">US Policy for a Multipolar Age</div>
      <div class="front__author">DANIEL P. WHITCOMBE</div>
      <div class="front__affiliation">(Long Horizon Project, Harold Lindqvist<br>Center on Global Stability)</div>
    </section>
  </div>
</body>
</html>
```